Stationary design for new high end strategy and business consulting company

We need a stationary design (incorporating business card, letter head, consultant profile, envelope, invoice etc.) for a new company called VERAMOND that is based in Australia.

Company provides high end strategy consulting/ advisory services - business insight - to the professional services, financial services, legal and health industries - in the areas of:
- strategy
- business transformation
- performance and profitability improvement
- commercial negotiation and procurement.

to enable companies to deliver an exceptional client experience for minimum cost, differentiate themselves in the market and maximize profitability

Design needs to be simple, stylish and sophisticated, bold and engaging. It should convey growth and prosperity; intelligent insight into how to make a company better and be more profitable; unique business insight.

Business cards should feature VERAMOND prominently as well as our Director’s name “Marcella Dovric”

Other contact details are as follows:
Mob: 0467 203 518
Email: madovric@veramondgrp.example
Web: www.veramondgrp.example

Colour pallet should incorporate lime green, dark greys, silver/ white

Target Market(s)

Law Firms
Banks, Investment Banks and Financial Services Companies
Healthcare companies that own hospitals, nursing homes, radiology and pathology services

Industry/Entity Type

Financial

Font styles to use
Sans Serif

Colors
add136
5c5c5c
e9e9e9

```html
<!DOCTYPE html>
<html lang="en">
<head>
<meta charset="utf-8">
<title>Veramond Stationery</title>
<link rel="stylesheet" href="https://fonts.googleapis.com/css2?family=Open+Sans:wght@600;700&display=swap">
<style>
  :root {
    --lime: #add136;
    --charcoal: #3f3f41;
    --grey: #5c5c5c;
    --silver: #e9e9e9;
    --paper: #ffffff;
    --paper-back: #fafafa;
    --backdrop: #e3e2e5;
    --ghost: #efefef;
  }
  * { box-sizing: border-box; margin: 0; padding: 0; }
  html, body { width: 1200px; height: 900px; overflow: hidden; }
  body {
    background: var(--backdrop);
    font-family: "Open Sans", Arial, sans-serif;
    position: relative;
  }

  /* Envelope front */
  .envelope-front {
    position: absolute; left: 138px; top: 135px;
    width: 648px; height: 288px;
    background: var(--paper); overflow: hidden;
  }
  .envelope-front .ghost-name {
    position: absolute; right: -24px; bottom: -34px;
    font-size: 128px; font-weight: 700; letter-spacing: 2px;
    color: var(--ghost); line-height: 1;
  }
  .sender {
    position: absolute; left: 38px; top: 30px;
    color: var(--charcoal);
  }
  .sender .mark {
    display: block; width: 40px; height: 40px;
    background: var(--charcoal); margin-bottom: 24px;
  }
  .sender .brand-name {
    font-size: 21px; font-weight: 700; letter-spacing: 0.5px; line-height: 1;
  }
  .sender .contact { margin-top: 9px; line-height: 1.15; }
  .sender .phone { font-size: 10px; font-weight: 700; }
  .sender .email, .sender .web { font-size: 7.5px; font-weight: 700; }

  /* Envelope back */
  .envelope-back {
    position: absolute; left: 138px; top: 472px;
    width: 648px; height: 288px;
    background: var(--paper-back);
  }
  .envelope-back .flap { position: absolute; left: 0; top: 0; }
  .envelope-back .flap-name {
    position: absolute; left: 0; top: 38px; width: 648px;
    text-align: center; font-size: 24px; font-weight: 700;
    letter-spacing: 1px; color: rgba(255,255,255,0.55);
  }

  /* Pen */
  .pen {
    position: absolute; left: 918px; top: 148px;
    width: 38px; height: 570px;
    background: var(--paper); border-radius: 19px 19px 10px 10px;
  }
  .usb {
    position: absolute; left: 1040px; top: 168px;
    width: 72px; height: 272px;
    background: var(--paper); border-radius: 30px 30px 18px 18px;
  }
  .imprint {
    position: absolute; writing-mode: vertical-rl;
    font-size: 19px; font-weight: 700; letter-spacing: 1px;
    color: var(--charcoal);
  }
  .pen .imprint { left: 8px; top: 282px; }
  .usb .imprint { left: 25px; top: 108px; font-size: 17px; }
</style>
</head>
<body>

  <section class="envelope-front" aria-label="Envelope front">
    <span class="ghost-name" aria-hidden="true">VERAMOND</span>
    <div class="sender">
      <span class="mark"></span>
      <div class="brand-name">VERAMOND</div>
      <div class="contact">
        <div class="phone">0467 203 518</div>
        <div class="email">madovric@veramondgrp.example</div>
        <div class="web">www.veramondgrp.example</div>
      </div>
    </div>
  </section>

  <section class="envelope-back" aria-label="Envelope back">
    <svg class="flap" width="648" height="114" viewBox="0 0 648 114" aria-hidden="true">
      <polygon points="0,0 648,0 596,114 52,114" fill="#add136"/>
    </svg>
    <div class="flap-name">VERAMOND</div>
  </section>

  <div class="pen" aria-label="Branded pen">
    <span class="imprint">VERAMOND</span>
  </div>

  <div class="usb" aria-label="Branded USB drive">
    <span class="imprint">VERAMOND</span>
  </div>

</body>
</html>
```